Business Card & Word Docs from existing Logo

We need a business card with typical information plus layout to include electrical contractors license number, VONEL license and KMP license. We would like a word document layout for a proposal document, opening page with logo and design basic information; proposal to and proposal from and project name and number. Small basic single page letter for general documents. Email signature with logo.

We are an electrical, refrigeration and automation contractor. We work with reducing energy consumption for our customers and complex process solutions in electrical, refrigeration and automation.

Reason: Final changes/ revisions to designs.

Target Market(s)

Industrial and commercial businesses that require more than your average contractor.

Industry/Entity Type

Electrical

Requirements
Must have
• Propsal document must have a full opening page.

```html
<!DOCTYPE html>
<html lang="en">
<head>
<meta charset="utf-8">
<title>Frostline Contracting – Proposal Template</title>
<link rel="stylesheet" href="https://fonts.googleapis.com/css2?family=Open+Sans:wght@400;600;700&family=Roboto+Condensed:wght@400;700&display=swap">
<style>
  :root {
    --stage: #000000;
    --paper: #ffffff;
    --field: #f2f7fa;
    --ink: #1a1a1a;
    --muted: #6b6b6b;
    --brand: #1fa3d3;
    --brand-mark: #3bbf4a;
  }
  * { margin: 0; padding: 0; box-sizing: border-box; }
  html, body { width: 1200px; height: 900px; overflow: hidden; background: var(--stage); }
  .stage { position: relative; width: 1200px; height: 900px; }

  .sheet { position: absolute; top: 75px; width: 530px; height: 750px; background: var(--paper); }
  .sheet--cover { left: 42px; }
  .sheet--continuation { left: 628px; }

  .brand { position: absolute; top: 27px; right: 30px; display: flex; align-items: center; gap: 8px; }
  .brand__dot { width: 36px; height: 36px; border-radius: 50%; background: var(--brand-mark); }
  .brand__name { font-family: "Open Sans", sans-serif; font-weight: 600; color: var(--brand); line-height: 1; }
  .brand__name span { display: block; }
  .brand__primary { font-size: 21px; letter-spacing: -0.3px; }
  .brand__secondary { font-size: 10.5px; letter-spacing: 3.4px; margin-top: 3px; }

  .contact { position: absolute; top: 84px; right: 30px; text-align: right;
    font-family: "Roboto Condensed", sans-serif; font-size: 8px; line-height: 10px; color: var(--ink); }
  .contact b { font-weight: 700; }

  .field { position: absolute; }
  .field__label { font-family: "Open Sans", sans-serif; font-weight: 700; font-size: 8px; color: var(--ink); height: 11px; }
  .field__box { height: 22px; background: var(--field); border-radius: 10px 10px 0 0; margin-top: 3px; }
  .field--to { left: 30px; top: 140px; width: 226px; }
  .field--from { left: 274px; top: 140px; width: 226px; }
  .field--project { left: 30px; top: 185px; width: 332px; }
  .field--number { left: 379px; top: 185px; width: 121px; }

  .body-panel { position: absolute; left: 30px; right: 30px; bottom: 28px; background: var(--field); border-radius: 10px; }
  .sheet--cover .body-panel { top: 242px; }
  .sheet--continuation .body-panel { top: 30px; }

  .folio { position: absolute; right: 30px; bottom: 14px; font-family: "Roboto Condensed", sans-serif;
    font-size: 8px; color: var(--muted); }
  .folio b { font-weight: 700; color: #4a4a4a; }
</style>
</head>
<body>
<main class="stage">
  <section class="sheet sheet--cover">
    <div class="brand">
      <div class="brand__dot"></div>
      <div class="brand__name">
        <span class="brand__primary">FROSTLINE</span>
        <span class="brand__secondary">CONTRACTING</span>
      </div>
    </div>
    <address class="contact" style="font-style:normal">
      PO Box 5678, Harbourton, Queensland, 4999<br>
      <b>T</b> 07 5550 1182 | <b>F</b> 07 5550 1183 | <b>M</b> 0400 555 274<br>
      office@frostline.com.au | www.frostline.com.au
    </address>

    <div class="field field--to"><div class="field__label">Proposal to</div><div class="field__box"></div></div>
    <div class="field field--from"><div class="field__label">Proposal from</div><div class="field__box"></div></div>
    <div class="field field--project"><div class="field__label">Project name</div><div class="field__box"></div></div>
    <div class="field field--number"><div class="field__label">Number</div><div class="field__box"></div></div>

    <div class="body-panel"></div>
    <p class="folio"><b>FROSTLINE CONTRACTING</b> Page 1 of X</p>
  </section>

  <section class="sheet sheet--continuation">
    <div class="body-panel"></div>
    <p class="folio"><b>FROSTLINE CONTRACTING</b> Page 2 of X</p>
  </section>
</main>
</body>
</html>
```